Business card for Quorvane LLC | ||
Design a business card for a geospatial startup | ||
Use same font as used in my logo | ||
Cutting-Edge Corporate Modern Professional Simple |
Peter Hollis | ||
Chief Technical Officer | ||
48 Linden Row Suite 200 Bramwick, ST, 55821-3307 |
hello@quorvane-mail.net | ||
www.quorvane-site.net | ||
I''l provide the actual information once we get rolling :) I'd like to incorporate the corporate logo onto the card. Please keep the colors in the logo. You can use any font that looks good. |

```html
<!DOCTYPE html>
<html lang="en">
<head>
<meta charset="utf-8">
<title>Quorvane LLC — Business Card</title>
<link rel="stylesheet" href="https://fonts.googleapis.com/css2?family=Open+Sans:wght@400;600;700&family=Tinos&display=swap">
<style>
  :root {
    --brand-blue: #1f5ea8;
    --band-blue: #2a5d9c;
    --brand-green: #7cbf2e;
    --ink: #2b2b2b;
    --rule: #9a9a9a;
    --card: #ffffff;
    --card-shade: #eef0f2;
  }
  * { margin: 0; padding: 0; box-sizing: border-box; }
  html, body { width: 1200px; height: 780px; overflow: hidden; }
  body { background: var(--card); font-family: "Open Sans", Arial, sans-serif; }

  .card {
    position: relative;
    width: 1200px;
    height: 780px;
    background: linear-gradient(160deg, var(--card) 55%, var(--card-shade) 100%);
    overflow: hidden;
  }

  .wordmark {
    position: absolute;
    left: 170px;
    top: 170px;
    display: flex;
    align-items: center;
    gap: 22px;
  }
  .wordmark-dot {
    width: 34px; height: 34px;
    border-radius: 50%;
    background: var(--brand-green);
  }
  .wordmark-name {
    font-weight: 700;
    font-size: 116px;
    line-height: 1;
    letter-spacing: -2px;
    color: var(--brand-blue);
  }

  .identity {
    position: absolute;
    right: 625px;
    top: 392px;
    text-align: right;
  }
  .identity-name {
    font-weight: 700;
    font-size: 37px;
    color: var(--brand-blue);
    line-height: 1.2;
  }
  .identity-title {
    font-weight: 700;
    font-size: 27px;
    color: var(--brand-green);
    margin-top: 14px;
  }

  .divider {
    position: absolute;
    left: 598px;
    top: 330px;
    width: 2px;
    height: 240px;
    background: var(--rule);
  }

  .contact {
    position: absolute;
    left: 622px;
    top: 330px;
    font-family: "Tinos", "Times New Roman", serif;
    color: var(--ink);
    font-size: 33px;
    line-height: 1.15;
  }
  .contact-address { margin-bottom: 36px; }
  .contact-line {
    display: flex;
    align-items: center;
    gap: 16px;
    margin-bottom: 18px;
  }
  .contact-icon { width: 30px; height: 30px; flex: none; }

  .footer-wave { position: absolute; left: 0; bottom: 0; width: 1200px; height: 260px; }

  .website {
    position: absolute;
    left: 330px;
    top: 694px;
    font-size: 32px;
    font-weight: 600;
    color: #ffffff;
  }
</style>
</head>
<body>
  <main class="card">
    <div class="wordmark">
      <span class="wordmark-name">Quorvane</span>
      <span class="wordmark-dot"></span>
    </div>

    <div class="identity">
      <p class="identity-name">Peter Hollis</p>
      <p class="identity-title">Chief Technical Officer</p>
    </div>

    <div class="divider"></div>

    <address class="contact" style="font-style:normal">
      <p class="contact-address">48 Linden Row Suite 200<br>Bramwick, ST, 55821-3307</p>
      <p class="contact-line">
        <svg class="contact-icon" viewBox="0 0 24 24" aria-hidden="true">
          <path d="M6.6 10.8a15.1 15.1 0 0 0 6.6 6.6l2.2-2.2a1 1 0 0 1 1-.25 11.4 11.4 0 0 0 3.6.57 1 1 0 0 1 1 1V20a1 1 0 0 1-1 1A17 17 0 0 1 3 4a1 1 0 0 1 1-1h3.5a1 1 0 0 1 1 1 11.4 11.4 0 0 0 .57 3.6 1 1 0 0 1-.25 1z" fill="#1f5ea8"/>
        </svg>
        (555) 301-4682
      </p>
      <p class="contact-line">
        <svg class="contact-icon" viewBox="0 0 24 24" aria-hidden="true">
          <circle cx="12" cy="12" r="11" fill="#1f5ea8"/>
          <text x="12" y="16.5" text-anchor="middle" font-family="Arial, sans-serif" font-weight="700" font-size="14" fill="#fff">@</text>
        </svg>
        hello@quorvane-mail.net
      </p>
    </address>

    <svg class="footer-wave" viewBox="0 0 1200 260" preserveAspectRatio="none" aria-hidden="true">
      <path d="M0 150 C 300 175, 700 120, 1200 10" fill="none" stroke="#7cbf2e" stroke-width="7"/>
      <path d="M0 175 C 320 200, 720 150, 1200 40 L 1200 260 L 0 260 Z" fill="#2a5d9c"/>
    </svg>

    <p class="website">www.quorvane-site.net</p>
  </main>
</body>
</html>
```